Interactive Children's Media Book Company Website Design

We need a website DESIGN (no coding required) for a new interactive children's media book company called Tovira Studios.

We develop high-quality interactive children's books for the iPad/iPhone that seeks to delight and inspire young and old alike. Our stories are filled with heart and spirit, and we seek to breathe magic back into books so that people fall back in love with reading.

Tovira means "butterfly" in Korean. It plays on the idea that a caterpillar metamorphoses into a butterfly - and in the same way, our readers are transformed through the journey of experiencing our interactive books.

We're looking for something based on the ATTACHED LOGO DESIGN for our company. A website that's professional, modern, fun and inviting; easy to read and not-cluttered, but still portraying the feeling of innocence and childhood.

We're looking for something that resonates the magical experience we want to create for our readers. Specific requirements on pages, tabs, content, etc are below.

• There are 7 tabs on the Homepage of the website: HOME, OUR GRANDPA, ABOUT US, CAREERS, NEWS, CONTACT US, SHOP. (But there is an extra page called YOUR GRANDPA, which will be a sub-page under Our Grandpa).

HOME
• Would be great to have some key images of our book (3-4 screen shots) as the key focus of the homepage that automatically scroll through every few seconds. (Placeholder image attached). The images would link to the “Our Grandpa” page.
• Company logo (attached to brief) and slogan: “A new era of children’s media” quite prominent on page.
• Key text content to be on page: “Tovira means “butterfly” in Korean. Just as a caterpillar transforms into a butterfly, Tovira Studios takes the reader on an unforgettable journey of metamorphosis through our stories. We turn children’s books into a high-quality interactive experience on mobile platforms - breathing magic back into books, and inspiring people to fall back in love with reading. Through our unique characters full of heart and spirit, our stories delight and inspire young and old alike.”
• Chirper & Pagebook Like & Pagebook page link icons.
• Section on Latest News with a few of the latest entries.
• Section on latest sister images & comments that visitors have posted, which takes you to the “Your Grandpa” page.

OUR GRANDPA
• The title for this page is “Our Grandpa Hums at Breakfast Time”
• There will be a little iPad/iPhone icon (placeholder attached) for this book.
• There will be a link to the App Store to buy the app book.
• Key text content on this page: “Our debut interactive media book is coming soon on the iPad and iPhone! “Our Grandpa Hums at Breakfast Time” touches on the beautiful and inextricable (albeit sometimes frustrating!) bond between sisters.”
• There will be a section on “Features” which lists all the various special features the app book includes.
• There will be a YouTube clip embedded into the page, which shows how the app book works.
• A section that says: “Do you have a sister who’s not like other sisters? Share a photo and tell us about her!” which links to the sub-page “Your Grandpa”.
• Under this, there may be the most recent few images submitted by the public, which when clicked on, would also link to the sub-page “Your Grandpa”.

YOUR GRANDPA
• The main text on the page: “Do you have a sister who’s not like other sisters? Share a photo and tell us about her!”
• Main body of the page is a gallery of all the photos that have been submitted. If you click on each of the images, you get the comments that people have submitted with the photos.
• The page would also have a Submit Comments Form, where people can upload a picture of their sister(s) and write a comment to accompany the image.

ABOUT US
• Introductory text on page: “It was a chance conversation at Harbourline Terminal, where two friends discovered they shared a dream to create quality children's media. Both of them were excited by the possibilities of using new digital platforms to inspire and educate a younger generation. From that idea Tovira Studios was born. We seek to be the chrysalis of story telling - to inspire the hearts and minds of our generation, and generations to come.”
• Section to “Join the Mailing List” where they can put their email address in and submit.
• Bios of 2x people with photos (bios in word doc attached) (do not have photos yet).

CAREERS
• The main text on the page: “We are always on the lookout for talented people to join our team. If you are a writer, illustrator, animator, iOS/android developer, musician, creative-writing translator - or have something special to offer Tovira Studios - we are keen to hear from you. Send us a message through the Contact Us tab above.”

NEWS
• Regular News page, with blog-type entries.

CONTACT US
• Online submit Contact Us form
• The main text on page: “Our studio is based in the Ember Craft Cooperative, 43 Pukeora Street, Marangai, Wellington. Ember is a professional, creative collective - with four separate studios, gallery, and retail store. For more information on Ember, visit: http://www.embercraftco.example.nz”
• “We would love to hear from you! Whether you have questions, ideas, comments, or just want to say hullo - please leave us a message and we will get back to you soon.”
• Including image of the premises (Ember image attached to brief).

SHOP
• Where visitors can purchase merchandise (t-shirts, mugs, etc) of the book/company.

```html
<!DOCTYPE html>
<html lang="en">
<head>
<meta charset="utf-8">
<title>Tovira Studios – Home</title>
<link rel="stylesheet" href="https://fonts.googleapis.com/css2?family=Open+Sans:ital,wght@0,400;0,700;1,400&family=Delius&display=swap">
<style>
  :root {
    --ink: #1a1a1a;
    --frame: #111111;
    --text-grey: #333333;
    --nav-top: #e9e9e9;
    --nav-bottom: #9c9c9c;
    --nav-divider: #c9c9c9;
    --sky: #b6e2f7;
    --sky-deep: #8fd2f2;
    --sky-tab: #a3dcf6;
    --pill-top: #f4f4f4;
    --pill-bottom: #bdbdbd;
    --brand: #8a7bb8;
    --lilac: #d8c8ee;
    --white: #ffffff;
  }
  html, body {
    margin: 0;
    width: 1200px;
    height: 900px;
    overflow: hidden;
    background: var(--white);
    font-family: "Open Sans", Arial, sans-serif;
    color: var(--ink);
  }
  .site {
    position: absolute;
    left: 64px; top: 88px;
    width: 1104px; height: 648px;
    box-sizing: border-box;
    border: 3px solid var(--frame);
    border-top-width: 6px;
    background: var(--white);
    overflow: hidden;
  }
  /* left intro column */
  .intro {
    position: absolute; left: 0; top: 0;
    width: 292px; height: 100%;
    background: linear-gradient(180deg, #ffffff 0%, #ffffff 52%, #e6e6e6 80%, #cfcfcf 100%);
  }
  .intro__glow {
    position: absolute; left: -20px; bottom: -20px;
    width: 190px; height: 170px;
    background: radial-gradient(ellipse at 40% 60%, rgba(200,170,235,.55), rgba(200,170,235,0) 70%);
  }
  .brand {
    position: absolute; left: 20px; top: 26px;
    display: flex; align-items: center; gap: 12px;
  }
  .brand__mark {
    width: 46px; height: 46px; border-radius: 50%;
    background: var(--lilac);
  }
  .brand__name {
    font-size: 30px; font-weight: 400; color: var(--brand);
    letter-spacing: .5px;
  }
  .intro__title {
    position: absolute; left: 16px; top: 182px; margin: 0;
    font-size: 16px; font-style: italic; font-weight: 400; color: var(--ink);
  }
  .intro__body {
    position: absolute; left: 16px; top: 206px; width: 266px; margin: 0;
    font-size: 15px; line-height: 23px; font-style: italic; color: var(--text-grey);
  }
  /* navigation */
  .nav {
    position: absolute; left: 293px; top: 0;
    width: 808px; height: 42px;
    display: flex; margin: 0; padding: 0; list-style: none;
    background: linear-gradient(180deg, var(--nav-top), var(--nav-bottom));
  }
  .nav__item {
    position: relative; flex: 1;
    text-align: center; line-height: 30px;
    font-size: 12.5px; font-weight: 700; color: var(--white);
    border-right: 1px solid var(--nav-divider);
    text-shadow: 0 1px 1px rgba(0,0,0,.25);
  }
  .nav__item:last-child { border-right: 0; }
  .nav__item--active { background: var(--sky-tab); }
  .nav__sub {
    position: absolute; left: 0; top: 42px; width: 100%;
    height: 40px; line-height: 40px;
    background: var(--sky-tab); color: var(--white);
    box-shadow: 0 2px 3px rgba(0,0,0,.2);
  }
  /* centre feature */
  .feature {
    position: absolute; left: 293px; top: 142px;
    width: 448px; height: 500px;
    background: var(--sky);
  }
  .feature__slides {
    position: absolute; left: 18px; top: 12px;
    width: 408px; height: 308px;
    border: 4px solid var(--frame);
    background: linear-gradient(180deg, #7cc4f0 0%, #bfe5fa 40%, #8cc46a 70%, #5f9d3e 100%);
  }
  .feature__slogan {
    position: absolute; left: 0; top: 336px; width: 100%; margin: 0;
    text-align: center;
    font-family: "Delius", "Comic Sans MS", cursive;
    font-size: 28px; font-weight: 400; color: var(--ink);
  }
  .social {
    position: absolute; left: 0; top: 394px;
    width: 100%; height: 106px;
    background: var(--sky-deep);
    display: flex;
  }
  .social__group { flex: 1; padding: 12px 0 0 26px; }
  .social__label {
    margin: 0 0 12px; font-size: 11px; font-weight: 700; color: var(--ink);
  }
  .social__row { display: flex; align-items: center; gap: 12px; }
  .social__square { width: 36px; height: 36px; background: #3b5a98; }
  .social__circle { width: 36px; height: 36px; border-radius: 50%; background: #dff3fc; }
  .social__button {
    padding: 5px 10px; border-radius: 4px;
    background: linear-gradient(180deg, #f7f7f7, #c6c6c6);
    border: 1px solid #999;
    font-size: 15px; color: #3b5a98;
  }
  /* right sidebar */
  .sidebar {
    position: absolute; left: 741px; top: 42px;
    width: 360px; height: 600px;
  }
  .panel-head {
    position: absolute; left: 0; width: 100%; height: 32px;
    background: var(--sky);
  }
  .panel-head__pill {
    position: absolute; top: 4px; height: 24px; line-height: 24px;
    padding: 0 20px;
    background: linear-gradient(180deg, var(--pill-top), var(--pill-bottom));
    border: 1px solid #8f8f8f; border-radius: 2px;
    font-size: 12.5px; font-weight: 700; color: #555;
  }
  .panel-head__deco { position: absolute; top: 0; width: 30px; height: 30px; }
  .sidebar__community { position: absolute; top: 32px; left: 0; width: 100%; height: 246px; background: var(--white); }
  .sidebar__photo {
    position: absolute; left: 8px; top: 22px;
    width: 136px; height: 140px;
    border: 2px solid #444;
    background: linear-gradient(180deg, #f2b98a 0%, #f6d6b6 60%, #c8a3d8 100%);
  }
  .blurb {
    margin: 0; font-size: 10px; line-height: 21px; color: var(--ink);
  }
  .sidebar__community .blurb { position: absolute; left: 200px; top: 14px; width: 150px; }
  .sidebar__news { position: absolute; top: 310px; left: 0; width: 100%; height: 290px; }
  .sidebar__news .blurb { position: absolute; top: 14px; width: 152px; }
  .caption {
    position: absolute; left: 0; top: 778px; width: 1200px; margin: 0;
    text-align: center; font-size: 17px; color: var(--ink);
    padding-right: 32px; box-sizing: border-box;
  }
</style>
</head>
<body>
  <main class="site">
    <section class="intro">
      <div class="intro__glow"></div>
      <div class="brand">
        <span class="brand__mark"></span>
        <span class="brand__name">Tovira Studios</span>
      </div>
      <h2 class="intro__title">Tovira means “Butterfly” in Korean.....</h2>
      <p class="intro__body">Just as a caterpillar transforms into a butterfly, Tovira Studios takes the reader on an unforgettable journey of metamorphosis through our stories. We turn childrens books into high quality interactive experience on mobile platform - breathing magic back into books , and inspiring people to fall back in love with reading. Through our unique characters full of heart and spirit, our stories delight and inspire young and old alike.</p>
    </section>

    <ul class="nav">
      <li class="nav__item">Home</li>
      <li class="nav__item nav__item--active">Our Grandpa
        <div class="nav__sub">Your Grandpa</div>
      </li>
      <li class="nav__item">About Us</li>
      <li class="nav__item">Careers</li>
      <li class="nav__item">News</li>
      <li class="nav__item">Contact Us</li>
      <li class="nav__item">Shop</li>
    </ul>

    <section class="feature">
      <div class="feature__slides" role="img" aria-label="Book screenshot slideshow: a girl bouncing on a trampoline in a sunny backyard with a house, tree and dog kennel"></div>
      <h1 class="feature__slogan">A New Era of Children’s Media</h1>
      <div class="social">
        <div class="social__group">
          <p class="social__label">LIKE OUR PAGEBOOK PAGE</p>
          <div class="social__row">
            <span class="social__square"></span>
            <span class="social__button">Pagebook</span>
          </div>
        </div>
        <div class="social__group">
          <p class="social__label">FOLLOW US ON CHIRPER</p>
          <div class="social__row">
            <span class="social__circle"></span>
            <span class="social__button">Chirper</span>
          </div>
        </div>
      </div>
    </section>

    <aside class="sidebar">
      <div class="panel-head" style="top:0">
        <span class="panel-head__pill" style="left:80px">YOUR GRANDPA NEWS</span>
        <span class="panel-head__deco" role="img" aria-label="Smiling sun illustration" style="left:266px;background:radial-gradient(circle,#ffd93a 55%,rgba(255,217,58,0) 72%)"></span>
      </div>
      <div class="sidebar__community">
        <div class="sidebar__photo" role="img" aria-label="Visitor-submitted picture of a red-haired character"></div>
        <p class="blurb">Lorem ipsum dolor sit amet, consectetur adipiscing elit. Suspendisse vehicula pretium sapien, non pellentesque nisl semper nec. Aenean ornare, augue eu egestas tincidunt,</p>
      </div>
      <div class="panel-head" style="top:278px">
        <span class="panel-head__deco" role="img" aria-label="Small butterfly decoration" style="left:16px;background:linear-gradient(135deg,#b9a2e6,#e7dcf7)"></span>
        <span class="panel-head__pill" style="left:90px">LATEST TOVIRA NEWS</span>
        <span class="panel-head__deco" role="img" aria-label="Small butterfly decoration" style="left:312px;background:linear-gradient(135deg,#b9a2e6,#e7dcf7)"></span>
      </div>
      <div class="sidebar__news">
        <p class="blurb" style="left:18px">Lorem ipsum dolor sit amet, consectetur adipiscing elit. Suspendisse vehicula pretium sapien, non pellentesque nisl semper nec. Aenean ornare, augue eu egestas tincidunt,</p>
        <p class="blurb" style="left:196px">Lorem ipsum dolor sit amet, consectetur adipiscing elit. Suspendisse vehicula pretium sapien, non pellentesque nisl semper nec. Aenean ornare, augue eu egestas tincidunt,</p>
      </div>
    </aside>
  </main>
  <p class="caption">Home Page</p>
</body>
</html>
```